Golden Coat All-Purpose Breading Bag Design

Our client, Halvern Food Products, is looking to re-design the packaging for their product, Pellow's Golden Coat. Goldn Coat is an all-purpose food breading mix.

Halvern Foods has a registered trademark for this product, but they have not been using it for this particular 10 pound bag. They want to get the trademark onto the bag and also give the bag an updated look. They would like to continue to use the same red and blue colors. This 10 pound bag is not available on store shelves; it is sold to food service distributors who sell to restaurants.

All of the copy on the existing bag is still relevant, so we will want to incoprporate it into the bag design. Once these bags are filled with product, the tops get folded over about 1 inch and then sewn shut with thread.

Eventually, we will need the design applied to the Bag Template file attached, but that isn't important until a design is selected.

Target Market(s)

Restaurants

Industry/Entity Type

Food Manufacturing

Colors
0054AA
0677BA
7BADD7
CADEEF
E8F1F8
EB3D1F
EC4F4E
F09395
F8D3D4
FCEDEE

Requirements
Must have
• Trademark introduced to the design

```html
<!DOCTYPE html>
<html lang="en">
<head>
<meta charset="utf-8">
<title>Pellow's Golden Coat – Bag Panels</title>
<link href="https://fonts.googleapis.com/css2?family=Oswald:wght@300;400;600;700&family=Arimo:wght@400;700&display=swap" rel="stylesheet">
<style>
  :root{
    --blue:#0054AA;
    --blue-mid:#0677BA;
    --blue-light:#7BADD7;
    --blue-pale:#CADEEF;
    --red:#EB3D1F;
    --white:#ffffff;
    --stage:#e9eaec;
    --display:'Oswald', sans-serif;
    --body:'Arimo', sans-serif;
  }
  *{box-sizing:border-box;margin:0;padding:0}
  html,body{width:1200px;height:2309px;overflow:hidden;background:var(--stage)}
  .canvas{position:relative;width:1200px;height:2309px}

  .panel{position:absolute;background:var(--white);box-shadow:0 2px 10px rgba(0,0,0,.12);overflow:hidden}
  .panel--front{left:60px;top:60px;width:520px;height:1000px}
  .panel--back{left:620px;top:60px;width:520px;height:1000px}
  .panel--side-story{left:60px;top:1120px;width:340px;height:1000px}
  .panel--side-directions{left:430px;top:1120px;width:340px;height:1000px}
  .panel--flap{left:800px;top:1120px;width:340px;height:240px;display:flex;align-items:center;justify-content:center}

  .band{position:absolute;left:78px;right:78px;top:0;bottom:0;display:flex;flex-direction:column;align-items:stretch}
  .brand-block{background:var(--blue);display:flex;align-items:flex-end;justify-content:center;padding-bottom:34px}
  .brand-name{font-family:var(--display);font-weight:600;color:var(--white);font-size:76px;line-height:1;letter-spacing:1px}
  .maker-strip{background:var(--red);color:var(--white);text-align:center;font-family:var(--body);padding:14px 10px 16px}
  .maker-strip .maker{font-size:17px;letter-spacing:.3px}
  .maker-strip .address{font-size:12px;margin-top:6px;line-height:1.25}

  .product-name{font-family:var(--display);font-weight:700;color:var(--blue);text-align:center;line-height:.98}
  .product-name .line-top{display:block}
  .product-name .line-bottom{display:flex;align-items:center;justify-content:center;gap:16px}
  .product-name .rule{display:inline-block;height:8px;background:var(--red)}

  .front .product-name{font-size:118px;margin-top:44px}
  .front .product-name .rule{width:72px}
  .tag-primary{font-family:var(--display);font-weight:300;color:var(--red);font-size:34px;text-align:center;margin-top:24px}
  .tag-secondary{font-family:var(--display);font-weight:400;color:var(--blue);font-size:25px;text-align:center;margin-top:2px}
  .slogan-box{background:var(--red);color:var(--white);font-family:var(--display);font-weight:300;font-size:24px;text-align:center;line-height:1.35;padding:16px 8px;margin-top:30px}
  .slogan-box b{font-weight:600}
  .info-block{background:var(--blue);flex:1;padding:26px 22px 20px;color:var(--white);font-family:var(--body);display:flex;flex-direction:column}
  .cook-row{display:flex;align-items:center;justify-content:space-between;gap:10px}
  .cook-row p{font-size:18px;line-height:1.25}
  .timer{display:flex;align-items:center;gap:4px}
  .timer-tag{background:var(--white);color:var(--blue);font-family:var(--display);font-weight:600;font-size:13px;line-height:1;padding:4px 5px;text-align:center}
  .ingredients{border:2px dashed var(--white);font-size:13px;line-height:1.35;padding:12px 14px;margin-top:22px}
  .net-wt{font-family:var(--display);font-weight:600;text-align:center;font-size:14px;margin-top:auto}
  .net-wt b{font-size:22px}

  .back .brand-block{height:200px;padding-bottom:50px}
  .back .product-name{font-size:130px;margin-top:60px}
  .back .product-name .rule{width:96px}
  .use-box{background:var(--red);color:var(--white);text-align:center;margin-top:42px;padding:24px 10px 20px;font-family:var(--display);font-weight:300}
  .use-box .use-line{font-size:22px;line-height:1.25}
  .use-box .use-line b{font-weight:600;font-size:32px}
  .use-box small{display:block;font-size:15px;margin-top:8px}
  .formula-box{background:var(--blue-mid);color:var(--white);text-align:center;padding:18px 10px 22px;font-family:var(--body);font-size:15px;line-height:1.3}
  .food-icons{display:flex;justify-content:center;gap:10px;margin-top:16px}
  .food-icon{width:54px;height:54px;border-radius:50%;border:2px solid var(--white);background:var(--blue-light)}
  .foods-list{background:var(--blue);flex:1;color:var(--white);font-family:var(--body);font-size:18px;text-align:center;line-height:1.55;padding:26px 10px}

  .side{position:absolute;left:40px;right:40px;top:0;bottom:0;display:flex;flex-direction:column}
  .side .brand-block{height:220px;padding-bottom:26px}
  .side .brand-name{font-size:52px}
  .side-body{flex:1;border:2px solid var(--blue-light);border-top:none;margin:0 -12px 40px;padding:30px 22px 20px;display:flex;flex-direction:column}
  .side .product-name{font-size:78px;color:var(--red)}
  .side .product-name .rule{width:46px;height:6px;background:var(--blue)}
  .story{font-family:var(--body);color:var(--blue);font-size:15px;line-height:1.3;text-align:justify;margin-top:26px}
  .side .timer{margin-top:auto;justify-content:center}

  .headline-red{font-family:var(--display);font-weight:700;color:var(--red);font-size:54px;line-height:1;text-align:center}
  .directions-bar{background:var(--blue);color:var(--white);font-family:var(--body);font-size:14px;text-align:center;padding:6px;margin-top:24px;letter-spacing:.5px}
  .steps{list-style:none;margin-top:22px;font-family:var(--body);color:var(--blue);font-size:20px;line-height:1.2}
  .steps li{position:relative;padding-left:20px;margin-bottom:16px}
  .steps li::before{content:"";position:absolute;left:0;top:7px;width:8px;height:8px;border-radius:50%;background:var(--red)}
  .steps .note{display:block;color:var(--red);font-size:14px;margin-top:8px;line-height:1.25}
  .best{font-family:var(--body);text-align:center;margin-top:18px}
  .best strong{display:block;color:var(--red);font-size:15px}
  .best span{color:var(--blue);font-size:16px}

  .flap-label{width:290px;text-align:center;border:2px solid var(--blue-light);padding:22px 10px}
  .flap-label .brand-name{color:var(--red);font-size:48px}
  .flap-label p{font-family:var(--display);font-weight:300;color:var(--red);font-size:17px;line-height:1.35;margin-top:10px}
  .flap-label p b{font-weight:600;color:var(--blue)}
</style>
</head>
<body>
<main class="canvas">

  <!-- Front panel -->
  <section class="panel panel--front front" aria-label="Front panel">
    <div class="band">
      <div class="brand-block" style="height:250px"><span class="brand-name">Pellow's</span></div>
      <div class="maker-strip">
        <div class="maker">BY HALVERN FOOD PRODUCTS</div>
        <div class="address">418 alder lane<br>cedar falls, iowa 50613</div>
      </div>
      <h1 class="product-name"><span class="line-top">GOLDEN</span><span class="line-bottom"><span class="rule"></span>COAT<span class="rule"></span></span></h1>
      <p class="tag-primary">ALL-PURPOSE BREADING</p>
      <p class="tag-secondary">SEALS JUICE IN - GREASE OUT</p>
      <p class="slogan-box">CHICKEN FRIED THE <b>GOLDEN COAT</b> WAY<br>IS FRIED CHICKEN <b>THE RIGHT</b> WAY</p>
      <div class="info-block">
        <div class="cook-row">
          <p>Cookes two pounds<br>chicken well done in<br>10 minuts &nbsp;(deep fat)</p>
          <div class="timer">
            <svg width="62" height="62" viewBox="0 0 62 62" aria-hidden="true">
              <rect x="27" y="1" width="8" height="6" fill="#EB3D1F"/>
              <circle cx="31" cy="35" r="24" fill="#fff" stroke="#EB3D1F" stroke-width="5"/>
              <text x="31" y="44" text-anchor="middle" font-family="Oswald, sans-serif" font-weight="700" font-size="24" fill="#EB3D1F">10</text>
            </svg>
            <span class="timer-tag">DEEP<br>FAT</span>
          </div>
        </div>
        <p class="ingredients"><b>INGREDIENTS:</b> flour, salt, non-fat milk solids, egg yolk, &nbsp;packing powder, corn starch, sugar and peper.</p>
        <p class="net-wt">NET WT <b>10</b> LBS</p>
      </div>
    </div>
  </section>

  <!-- Back panel -->
  <section class="panel panel--back back" aria-label="Back panel">
    <div class="band">
      <div class="brand-block"><span class="brand-name">Pellow's</span></div>
      <h2 class="product-name"><span class="line-top">GOLDEN</span><span class="line-bottom"><span class="rule"></span>COAT<span class="rule"></span></span></h2>
      <div class="use-box">
        <p class="use-line">for <b>Deep Fat</b></p>
        <p class="use-line">and <b>Pan Frying</b></p>
        <small>(Slightly &nbsp;Longer On Pan Frying)</small>
      </div>
      <div class="formula-box">
        THIS FORMULA IS AN ALL-DRY MIX<br>TO BE USED ON ANYTHING BREADED
        <div class="food-icons">
          <span class="food-icon" role="img" aria-label="Chicken icon"></span>
          <span class="food-icon" role="img" aria-label="Fish icon"></span>
          <span class="food-icon" role="img" aria-label="Steak icon"></span>
          <span class="food-icon" role="img" aria-label="Shrimp icon"></span>
          <span class="food-icon" role="img" aria-label="Onion rings icon"></span>
        </div>
      </div>
      <p class="foods-list">CHICKEN &bull; STEAKS &bull; CHOPS<br>TENDERLION &bull; FISH &bull; SHRIMP<br>OYSTERS &bull; OTHER SEA FOODS<br>ONION RINGS &bull; VEGTEABLES</p>
    </div>
  </section>

  <!-- Side panel: product story -->
  <section class="panel panel--side-story" aria-label="Side panel, product description">
    <div class="side">
      <div class="brand-block"><span class="brand-name">Pellow's</span></div>
      <div class="side-body">
        <h2 class="product-name"><span class="line-top">GOLDEN</span><span class="line-bottom"><span class="rule"></span>COAT<span class="rule"></span></span></h2>
        <p class="story">golden coat is a prepared formula of pure foods that enables you to fry chicken from the raw to the well done in ten minutes. It seals in all the natural juice and creates a very thin golden coating which the fat does not penetrate - thereby using much less fat yhan ordinary frying methods. this formula is an all-dry mix to be used on anything breaded - fish, oysters, shrimp, veal and chicken fried teak.</p>
        <div class="timer">
          <svg width="70" height="70" viewBox="0 0 62 62" aria-hidden="true">
            <rect x="27" y="1" width="8" height="6" fill="#EB3D1F"/>
            <circle cx="31" cy="35" r="24" fill="#fff" stroke="#EB3D1F" stroke-width="5"/>
            <text x="31" y="44" text-anchor="middle" font-family="Oswald, sans-serif" font-weight="700" font-size="24" fill="#EB3D1F">10</text>
          </svg>
          <span class="timer-tag" style="background:var(--blue);color:var(--white)">DEEP<br>FAT</span>
        </div>
      </div>
    </div>
  </section>

  <!-- Side panel: directions -->
  <section class="panel panel--side-directions" aria-label="Side panel, directions">
    <div class="side">
      <div class="brand-block"><span class="brand-name">Pellow's</span></div>
      <div class="side-body">
        <h2 class="headline-red">NOTHING<br>TO ADD</h2>
        <p class="directions-bar">DIRECTIONS</p>
        <ul class="steps">
          <li>Wet all foods in water.</li>
          <li>Place in dry dip, coating thoroughly.</li>
          <li>Fry (350o f).<span class="note">CHICKEN 1.5 TO 2 POUNDS 10 MINUTES, OVER 2 POUNDS SLIGHTLY LONGER.</span></li>
        </ul>
        <p class="best"><strong>FOR BEST RESULTS</strong><span>Double dip onion<br>rings &amp; oysters.</span></p>
      </div>
    </div>
  </section>

  <!-- Bottom flap -->
  <section class="panel panel--flap" aria-label="Bottom flap">
    <div class="flap-label">
      <span class="brand-name">Pellow's</span>
      <p>CHICKEN FRIED THE <b>GOLDEN COAT</b> WAY<br>IS FRIED CHICKEN <b>THE RIGHT</b> WAY</p>
    </div>
  </section>

</main>
</body>
</html>
```